Ireland’s Oldest Thatched Pub. Irish Poítín Label

The Larchmoor Inn is a Ireland’s Oldest Thatched Pub dating back to 1654.
We Previously has launched our own Irish Whiskey under the brand name “Larchmoor 1712” Single Malt Irish Whiskey.
We are now planning to launch our own Irish Poítín and would like a bottle label designed. I have attached images of our Whiskey labels and images if the finished bottle.

```html
<!DOCTYPE html>
<html lang="en">
<head>
<meta charset="utf-8">
<title>Larchmoor 1712 Irish Poitín Label</title>
<link rel="stylesheet" href="https://fonts.googleapis.com/css2?family=Rye&family=UnifrakturMaguntia&family=Libre+Caslon+Text:wght@400;700&display=swap">
<style>
  :root {
    --page: #f1f0ee;
    --paper: #f7f6f3;
    --ink: #2f2f2f;
    --ink-soft: #4a4a4a;
    --gold: #a88a5a;
    --gold-dark: #8d7248;
    --gold-light: #d9c7a4;
    --gold-pale: #ece3d2;
    --tab: #1f1f1f;
    --white: #ffffff;
  }
  * { margin: 0; padding: 0; box-sizing: border-box; }
  html, body { width: 900px; height: 1200px; overflow: hidden; background: var(--page); }
  .canvas { position: relative; width: 900px; height: 1200px; }

  .label {
    position: absolute; left: 60px; top: 66px; width: 780px; height: 1068px;
    background: var(--paper);
    box-shadow: 0 2px 10px rgba(0,0,0,0.08);
    overflow: hidden;
  }

  .engraving {
    position: absolute; left: 14px; right: 14px; top: 14px; height: 720px;
    background:
      radial-gradient(ellipse at 50% 88%, rgba(168,138,90,0.55), rgba(168,138,90,0) 60%),
      linear-gradient(180deg, var(--gold-pale) 0%, #f3ede2 40%, var(--gold-light) 100%);
  }

  .brand-tab {
    position: absolute; left: 50%; top: 0; transform: translateX(-50%);
    width: 150px; height: 96px; background: var(--tab);
    display: flex; align-items: center; justify-content: center;
    color: var(--white);
    font-family: "Libre Caslon Text", serif; font-weight: 400;
    font-size: 17px; letter-spacing: 2px;
  }

  .ribbon {
    position: absolute; left: 128px; top: 120px; width: 524px; height: 74px;
  }
  .ribbon-text {
    position: absolute; inset: 0; display: flex; justify-content: center; align-items: center;
    font-family: "Libre Caslon Text", serif; font-size: 34px; letter-spacing: 5px;
    color: var(--white); padding-bottom: 4px; white-space: nowrap;
  }

  .age {
    position: absolute; left: 0; right: 0; top: 190px;
    display: flex; justify-content: center; align-items: center; gap: 14px;
    font-family: "Libre Caslon Text", serif; color: var(--ink);
  }
  .age-word { font-size: 22px; letter-spacing: 3px; margin-top: 22px; }
  .age-number { font-family: "Rye", serif; font-size: 76px; line-height: 1; }

  .brand-name {
    position: absolute; left: 40px; right: 40px; top: 278px; text-align: center;
    font-family: "Rye", serif; font-size: 92px; line-height: 1;
    color: var(--ink); white-space: nowrap;
  }

  .year-pill {
    position: absolute; left: 50%; top: 396px; transform: translateX(-50%);
    width: 270px; height: 56px; border-radius: 28px; background: var(--white);
    display: flex; justify-content: center; align-items: center;
    font-family: "Libre Caslon Text", serif; font-weight: 700; font-size: 44px;
    color: var(--ink); letter-spacing: 3px;
  }

  .rule { position: absolute; left: 24px; right: 24px; height: 3px; background: var(--ink-soft); }
  .rule-top { top: 738px; }
  .rule-bottom { top: 892px; }

  .product-name {
    position: absolute; left: 0; right: 0; top: 752px; text-align: center;
    font-family: "UnifrakturMaguntia", serif; font-size: 118px; line-height: 1.1;
    color: var(--ink); white-space: nowrap;
  }

  .maker {
    position: absolute; left: 0; right: 0; top: 918px;
    display: flex; justify-content: center; align-items: center; gap: 22px;
    font-family: "Libre Caslon Text", serif; color: var(--ink-soft);
  }
  .maker-lines { text-align: center; white-space: nowrap; }
  .maker-company { font-size: 24px; letter-spacing: 1px; }
  .maker-place { font-size: 32px; letter-spacing: 2px; margin-top: 6px; }
  .leaf-mark { width: 34px; height: 34px; border-radius: 50%; background: var(--ink-soft); flex: none; }
</style>
</head>
<body>
<div class="canvas">
  <div class="label">
    <div class="engraving" role="img" aria-label="Engraved illustration of an old thatched cottage pub with ornamental flourishes"></div>

    <div class="brand-tab">LARCHMOOR</div>

    <div class="ribbon">
      <svg width="524" height="74" viewBox="0 0 524 74" aria-hidden="true">
        <path d="M0 14 L40 14 L40 70 L0 70 L16 42 Z" fill="#8d7248"/>
        <path d="M524 14 L484 14 L484 70 L524 70 L508 42 Z" fill="#8d7248"/>
        <path d="M30 6 Q262 -10 494 6 L494 60 Q262 44 30 60 Z" fill="#a88a5a" stroke="#2f2f2f" stroke-width="2"/>
      </svg>
      <div class="ribbon-text">SPECIAL RESERVE</div>
    </div>

    <div class="age">
      <span class="age-word">AGED</span>
      <span class="age-number">8</span>
      <span class="age-word">YEARS</span>
    </div>

    <div class="brand-name">LARCHMOOR</div>
    <div class="year-pill">1712</div>

    <div class="rule rule-top"></div>
    <div class="product-name">Irish Poitin</div>
    <div class="rule rule-bottom"></div>

    <div class="maker">
      <span class="leaf-mark" role="img" aria-label="Shamrock emblem"></span>
      <div class="maker-lines">
        <p class="maker-company">THE LARCHMOOR WHISKEY COMPANY</p>
        <p class="maker-place">COUNTY ANTRIM, IRELAND</p>
      </div>
      <span class="leaf-mark" role="img" aria-label="Shamrock emblem"></span>
    </div>
  </div>
</div>
</body>
</html>
```